Trifold Total Body Wellness pamphlet for dental patients

I had Chat GPT help create and layout a pamphlet to be used in my dental office. I placed the wording and would like a graphic designer to make it better so I can get it printed and start handing it out to patients. We are a science driven dental office with the goal of total body wellness. Our main colors our black, white and gray with red as an accent color. We like a modern and clean look. We are an established dental practice and would like to evolve the way we do things when science shows a better way. This pamphlet will help explain to our existing patients why we are doing things differently and how it will better help us treat the disease in their mouths.

```html
<!DOCTYPE html>
<html lang="en">
<head>
<meta charset="utf-8">
<title>Total Body Wellness Trifold</title>
<link href="https://fonts.googleapis.com/css2?family=Poppins:ital,wght@0,400;0,500;0,600;0,700;1,400&family=Great+Vibes&display=swap" rel="stylesheet">
<style>
:root{
  --accent:#c62832;
  --charcoal:#1d1d20;
  --slate:#6c6f75;
  --ink:#2a2b2e;
  --grey:#7d8087;
  --paper:#f4f4f5;
  --paper-warm:#efefee;
  --line:#d9dadd;
  --stage:#4a4a4a;
  --white:#ffffff;
}
*{box-sizing:border-box;margin:0;padding:0}
html,body{width:1200px;height:1005px;overflow:hidden;background:var(--stage);font-family:'Poppins',sans-serif;color:var(--ink)}
.side-label{position:absolute;left:0;width:1200px;text-align:center;color:#fff;font-size:17px;font-weight:400}
.spread{position:absolute;left:270px;width:660px;height:466px;display:flex;box-shadow:0 8px 18px rgba(0,0,0,.35)}
.panel{position:relative;width:220px;height:466px;overflow:hidden}
.center{text-align:center}
.rule{width:22px;height:2px;background:var(--charcoal);margin:6px auto}
.hair{height:1px;background:var(--line);margin:10px auto;width:110px}
.small{font-size:6px;line-height:1.6;color:var(--ink)}
.accent{color:var(--accent)}
.abs{position:absolute}

/* front panel 1 */
.mission{background:var(--paper);padding:22px 18px 0}
.mission h2{font-size:14px;font-weight:700;color:var(--accent);line-height:1.1}
.mission h3{font-size:10px;font-weight:500;color:var(--charcoal)}
.feature{display:flex;gap:8px;margin:12px 0 0 12px;align-items:flex-start}
.feature .ico{flex:0 0 24px;height:24px;border-radius:50%;background:#e8e8ea;border:1px solid var(--line);display:flex;align-items:center;justify-content:center}
.feature h4{font-size:7px;font-weight:600;color:var(--charcoal);margin-top:2px}
.feature p{font-size:5.6px;color:var(--grey);line-height:1.4}
.thanks{margin:18px 18px 0 18px;border-left:2px solid var(--accent);background:#e9e9ea;padding:9px 10px;font-size:6px;line-height:1.6}

/* front panel 2 */
.contact{background:var(--paper-warm);padding:30px 18px 0}
.brand-name{font-size:15px;font-weight:500;color:var(--ink);text-align:center;line-height:1.1}
.brand-tag{font-size:7px;font-weight:500;color:var(--grey);text-align:center;letter-spacing:1px}
.tagline{font-size:6.5px;font-weight:600;color:var(--charcoal);text-align:center;margin-top:8px}
.contact-line{display:flex;gap:8px;align-items:flex-start;margin:10px 0 0 28px;font-size:7px;line-height:1.4}
.socials{display:flex;gap:10px;justify-content:center;margin-top:10px}
.socials span{width:20px;height:20px;border-radius:50%;border:1px solid var(--line);background:#fff}

/* front panel 3 */
.cover{background:var(--slate);text-align:center;padding-top:40px}
.cover .quote-mark{font-size:54px;line-height:.7;color:var(--white);font-weight:700;height:26px}
.cover .lead{color:#fff;font-size:12px;line-height:1.35;margin-top:14px}
.cover .lead b{color:var(--charcoal);font-weight:700}

/* back panel 1 */
.why{background:var(--paper);padding:28px 14px 0}
.why h3{font-size:10px;font-weight:500;color:var(--charcoal)}
.why h2{font-size:12.5px;font-weight:700;color:var(--accent);line-height:1.2}
.why .motto{font-size:9px;font-weight:600;color:var(--accent);line-height:1.4;margin-top:4px}
.ring-label{font-size:3.8px;font-weight:600;color:var(--charcoal);text-align:center;line-height:1.2;position:absolute}

/* back panel 2 */
.difference{background:var(--slate);padding:26px 15px 0}
.difference h3{font-size:9.5px;font-weight:400;color:#fff}
.difference h2{font-size:9.5px;font-weight:700;color:var(--charcoal)}
.difference .rule{margin:6px 0;background:var(--accent)}
.diff-item{display:flex;gap:8px;margin-top:10px;align-items:flex-start}
.diff-item .ico{flex:0 0 24px;height:24px;border-radius:50%;background:var(--charcoal);border:2px solid #fff;display:flex;align-items:center;justify-content:center}
.diff-item .txt{border-left:1px solid var(--charcoal);padding-left:8px}
.diff-item h4{font-size:6.6px;font-weight:600;color:var(--charcoal)}
.diff-item p{font-size:5.2px;color:#fff;line-height:1.3}
.promise{margin-top:14px;border:1px solid #fff;border-radius:4px;padding:6px 8px;display:flex;gap:8px;align-items:center;width:174px}
.promise p{font-size:6.8px;font-weight:500;color:var(--charcoal);line-height:1.2}
.script{font-family:'Great Vibes',cursive;font-weight:400}
.band-dark{background:var(--charcoal);color:#fff}

/* back panel 3 */
.blueprint{background:#fff;padding:30px 14px 0}
.blueprint .title{font-size:10px;font-weight:500;color:var(--charcoal);line-height:1.2;margin-top:8px}
.blueprint .title-script{font-size:28px;color:var(--accent);line-height:1}
.blueprint .claim{font-size:6.6px;font-weight:500;color:var(--ink);line-height:1.5;margin-top:10px}
.blueprint .body{font-size:5.6px;line-height:1.75;width:100px;margin-top:8px}
.badge{display:flex;align-items:center;gap:4px;font-size:5px;font-weight:600;color:#fff;line-height:1.2}
</style>
</head>
<body>

<div class="side-label" style="top:4px">Front</div>

<section class="spread" style="top:32px">

  <article class="panel mission">
    <h2 class="center">OUR MISSION</h2>
    <h3 class="center">IS SIMPLE:</h3>
    <div class="rule"></div>
    <p class="small center" style="margin-top:8px">We don't follow trends. We follow science.<br>And we never stop looking for better<br>ways to care for you.</p>
    <div class="hair"></div>
    <div class="feature"><span class="ico"><svg width="12" height="12" viewBox="0 0 12 12"><circle cx="6" cy="4" r="2.5" fill="none" stroke="#1d1d20"/><path d="M3 11h6M6 7v4" stroke="#1d1d20"/></svg></span><div><h4>SCIENCE FIRST</h4><p>We base our decisions on research,<br>not assumptions.</p></div></div>
    <div class="feature"><span class="ico"><svg width="12" height="12" viewBox="0 0 12 12"><circle cx="6" cy="3" r="1.6" fill="#1d1d20"/><path d="M6 5v4M3 6h6M6 9l-2 2M6 9l2 2" stroke="#1d1d20"/></svg></span><div><h4>WHOLE BODY FOCUS</h4><p>Oral health is deeply connected to<br>your total body health.</p></div></div>
    <div class="feature"><span class="ico"><svg width="12" height="12" viewBox="0 0 12 12"><path d="M2 10V7M5 10V5M8 10V3M2 6l3-2 3-2" stroke="#1d1d20" fill="none"/></svg></span><div><h4>CONTINUOUS EVOLUTION</h4><p>We invest in education, technology,<br>and innovation so you always<br>receive the best care possible.</p></div></div>
    <div class="feature"><span class="ico"><svg width="12" height="12" viewBox="0 0 12 12"><circle cx="6" cy="4" r="2" fill="none" stroke="#1d1d20"/><path d="M2 11c0-3 8-3 8 0" stroke="#1d1d20" fill="none"/></svg></span><div><h4>BUILT ON TRUST</h4><p>We're honored to walk this journey<br>with you and your family.</p></div></div>
    <div class="thanks">Thank you for being part of our dental family. We're proud to care for you-<span class="accent">differently.</span></div>
  </article>

  <article class="panel contact">
    <p class="brand-name">Elena Marsh</p>
    <p class="brand-tag">DMD</p>
    <svg width="184" height="12" viewBox="0 0 184 12" style="display:block;margin:6px auto 0"><line x1="18" y1="6" x2="80" y2="6" stroke="#c62832"/><circle cx="92" cy="6" r="4" fill="none" stroke="#c62832"/><line x1="104" y1="6" x2="166" y2="6" stroke="#c62832"/></svg>
    <p class="tagline">SCIENCE. WELLNESS. SMILES.</p>
    <p class="small center" style="margin-top:8px">We're here to help you achieve a<br>healthier mouth and a healthier life. Let's<br>keep moving forward-together.</p>
    <div class="hair" style="width:150px;margin:14px auto 8px"></div>
    <div class="contact-line"><svg width="9" height="9" viewBox="0 0 10 10"><path d="M2 1l2 2-1 1.5c.8 1.5 1.5 2.2 3 3L7.5 6l2 2-1.5 1.5C4 9 1 6 .5 1.5z" fill="#1d1d20"/></svg><span>(555) 014-2278</span></div>
    <div class="contact-line"><svg width="9" height="10" viewBox="0 0 10 12"><path d="M5 0a4 4 0 0 1 4 4c0 3-4 8-4 8S1 7 1 4a4 4 0 0 1 4-4z" fill="#1d1d20"/><circle cx="5" cy="4" r="1.5" fill="#fff"/></svg><span>42 Linden Row<br>Fairview, MI 48100</span></div>
    <div class="contact-line"><svg width="9" height="8" viewBox="0 0 10 8"><rect width="10" height="8" fill="#1d1d20"/><path d="M0 0l5 4 5-4" stroke="#fff" fill="none"/></svg><span>www.elenamarshdental.com</span></div>
    <div class="hair" style="width:150px;margin:14px auto 10px"></div>
    <p class="tagline">CONNECT WITH US</p>
    <div class="socials"><span></span><span></span><span></span></div>
    <svg class="abs" style="left:0;bottom:0" width="220" height="70" viewBox="0 0 220 70"><path d="M0 0 C60 40 140 52 220 50 L220 70 L0 70 Z" fill="var(--charcoal)"/><path d="M0 6 C60 46 140 58 220 56 L220 70 L0 70 Z" fill="var(--slate)"/></svg>
  </article>

  <article class="panel cover">
    <div class="quote-mark">&ldquo;</div>
    <p class="lead">Because your<br>health is our<br><b>PRIORITY.</b></p>
    <svg width="70" height="10" viewBox="0 0 70 10" style="display:block;margin:10px auto 0"><line x1="0" y1="5" x2="26" y2="5" stroke="#fff" stroke-opacity=".7"/><path d="M35 8.5 31 5a2 2 0 0 1 4-2 2 2 0 0 1 4 2z" fill="none" stroke="#fff"/><line x1="44" y1="5" x2="70" y2="5" stroke="#fff" stroke-opacity=".7"/></svg>
    <div role="img" aria-label="3D tooth character holding a trophy on a round pedestal" class="abs" style="left:0;top:150px;width:220px;height:226px;background:radial-gradient(ellipse at 60% 55%,#f7f7f5 0%,#dcdcda 35%,rgba(108,111,117,0) 70%)"></div>
    <div role="img" aria-label="White marble tabletop" class="abs" style="left:0;bottom:0;width:220px;height:90px;background:linear-gradient(180deg,#e9e9eb,#c8c9cc)"></div>
  </article>
</section>

<div class="side-label" style="top:502px">Back</div>

<section class="spread" style="top:530px">

  <article class="panel why center">
    <h3>WHY WE DO</h3>
    <h2>THINGS DIFFERENTLY</h2>
    <div class="rule" style="background:var(--accent)"></div>
    <p class="small" style="font-size:5.6px">Dentistry is constantly evolving. As new research<br>and technology emerge, we evolve with it-so<br>you receive the <span class="accent">highest standard of care,</span><br>today and in the future.</p>
    <svg class="abs" style="left:30px;top:142px" width="160" height="140" viewBox="0 0 160 140"><circle cx="80" cy="70" r="56" fill="none" stroke="#d9dadd"/><circle cx="80" cy="70" r="32" fill="#fff"/><circle cx="80" cy="14" r="8" fill="#f4f4f5" stroke="#1d1d20"/><circle cx="24" cy="70" r="8" fill="#f4f4f5" stroke="#1d1d20"/><circle cx="136" cy="70" r="8" fill="#f4f4f5" stroke="#1d1d20"/><circle cx="80" cy="126" r="8" fill="#f4f4f5" stroke="#1d1d20"/><path d="M80 62 75 57a3 3 0 0 1 5-3 3 3 0 0 1 5 3z" fill="none" stroke="#c62832"/></svg>
    <p class="ring-label" style="left:82px;top:207px;width:56px;font-size:5px">OUR<br>COMMITMENT<br>TO YOU</p>
    <p class="ring-label" style="left:95px;top:166px;width:30px">SCIENCE<br>DRIVEN</p>
    <p class="ring-label" style="left:39px;top:222px;width:30px">EVIDENCE<br>BASED</p>
    <p class="ring-label" style="left:151px;top:222px;width:30px">TOTAL BODY<br>WELLNESS</p>
    <p class="ring-label" style="left:90px;top:278px;width:40px">PREVENT TREAT<br>TRANSFORM</p>
    <div class="hair" style="margin-top:188px;width:70px"></div>
    <p class="small" style="font-size:5.6px">We don't follow trends.<br>We follow science.</p>
    <p class="small" style="font-size:5.4px;font-style:italic;margin-top:6px">Our mission is simple:</p>
    <p class="motto">HEALTHY MOUTHS.<br>HEALTHY BODIES.<br>BETTER LIVES.</p>
    <p class="small" style="font-size:5.4px;margin-top:6px">Thank you for being part of our<br>dental family. We're proud to<br>care for you-differently.</p>
  </article>

  <article class="panel difference">
    <div role="img" aria-label="Faint white tooth" class="abs" style="right:12px;top:14px;width:56px;height:90px;border-radius:40% 40% 30% 30%;background:radial-gradient(ellipse,#e4e5e7,rgba(108,111,117,0) 70%)"></div>
    <h3>THE ELENA MARSH, DMD</h3>
    <h2>DIFFERENCE</h2>
    <div class="rule"></div>
    <p style="font-size:5.4px;color:#fff;line-height:1.6">We use advanced diagnostics and proven protocols to<br>identify and treat the root causes of oral health<br>issues-not just the symptoms.</p>
    <div class="diff-item"><span class="ico"><svg width="11" height="11" viewBox="0 0 12 12"><rect x="1" y="2" width="10" height="7" fill="none" stroke="#fff"/><path d="M4 11h4" stroke="#fff"/></svg></span><div class="txt"><h4>ADVANCED DIAGNOSTICS</h4><p>We utilize state-of-the-art technology<br>to detect problems earlier and more<br>accurately.</p></div></div>
    <div class="diff-item"><span class="ico"><svg width="11" height="11" viewBox="0 0 12 12"><ellipse cx="6" cy="6" rx="5" ry="3" fill="none" stroke="#fff"/><circle cx="6" cy="6" r="1.5" fill="#fff"/></svg></span><div class="txt"><h4>MINIMALLY INVASIVE APPROACH</h4><p>We preserve healthy tooth structure<br>and focus on long-term,<br>conservative care.</p></div></div>
    <div class="diff-item"><span class="ico"><svg width="11" height="11" viewBox="0 0 12 12"><path d="M6 1l4 2v3c0 3-4 5-4 5S2 9 2 6V3z" fill="none" stroke="#fff"/></svg></span><div class="txt"><h4>BIOCOMPATIBLE &amp; SAFE MATERIALS</h4><p>We choose materials that are safe<br>for your body and support your<br>overall wellness.</p></div></div>
    <div class="diff-item"><span class="ico"><svg width="11" height="11" viewBox="0 0 12 12"><circle cx="6" cy="3" r="1.8" fill="#fff"/><path d="M2 6l4 2 4-2M6 8v3" stroke="#fff" fill="none"/></svg></span><div class="txt"><h4>WHOLE-PERSON CARE</h4><p>We look at the connection between<br>your oral health and your total<br>body health.</p></div></div>
    <div class="diff-item"><span class="ico"><svg width="11" height="11" viewBox="0 0 12 12"><path d="M1 3h4l1 1 1-1h4v7H7l-1 1-1-1H1z" fill="none" stroke="#fff"/></svg></span><div class="txt"><h4>CONTINUOUS EDUCATION</h4><p>We stay on the leading edge of dental<br>research so you benefit from what's<br>new and what works.</p></div></div>
    <div class="promise"><svg width="18" height="16" viewBox="0 0 20 18"><path d="M10 16 2.5 8.5a4.3 4.3 0 0 1 7.5-4 4.3 4.3 0 0 1 7.5 4z" fill="none" stroke="#fff" stroke-width="1.4"/></svg><p>Better Dentistry. Better Health.<br><span class="script" style="font-size:11px;color:#fff">Better You.</span></p></div>
    <div class="abs band-dark" style="left:0;bottom:0;width:220px;height:64px;padding:12px 14px;font-size:9px;font-weight:500;line-height:1.9">
      <div style="display:flex;gap:7px;align-items:center"><svg width="10" height="10" viewBox="0 0 10 10"><path d="M2 1l2 2-1 1.5c.8 1.5 1.5 2.2 3 3L7.5 6l2 2-1.5 1.5C4 9 1 6 .5 1.5z" fill="#fff"/></svg>(555) 014-2278</div>
      <div style="display:flex;gap:7px;align-items:center"><svg width="10" height="10" viewBox="0 0 10 10"><circle cx="5" cy="5" r="4.3" fill="none" stroke="#fff"/><path d="M.7 5h8.6M5 .7c-2 2.5-2 6 0 8.6M5 .7c2 2.5 2 6 0 8.6" stroke="#fff" fill="none"/></svg>elenamarshdental.com</div>
    </div>
  </article>

  <article class="panel blueprint">
    <svg class="abs" style="right:0;top:0" width="90" height="116" viewBox="0 0 90 116"><path d="M22 0H90V116Z" fill="var(--charcoal)"/><path d="M0 0H22L90 116V122Z" fill="var(--accent)"/></svg>
    <div style="display:flex;align-items:center;gap:6px"><span style="width:18px;height:18px;border-radius:50%;border:1px solid var(--ink)"></span><span style="font-size:8px;font-weight:500;color:var(--ink);line-height:1.2">Elena Marsh<br>DMD</span></div>
    <p class="title">THE<br>WELLNESS</p>
    <p class="script title-script">Blueprint</p>
    <div class="rule" style="margin:6px 0"></div>
    <p class="claim">BECAUSE WE <span class="accent">KNOW MORE</span> TODAY<br>THAN WE DID YESTERDAY.</p>
    <p class="body">Advances in science and technology allow us to identify inflammation earlier, understand your unique oral microbiome, and personalize care in ways that simply weren't possible before.</p>
    <p class="body">Our commitment is to continually improve the quality of care we provide so you can enjoy a healthier mouth, a healthier body, and a better quality of life.</p>
    <div role="img" aria-label="Glossy white molar circled by a dark and red orbit ring" class="abs" style="left:118px;top:176px;width:94px;height:110px;background:radial-gradient(ellipse at 50% 45%,#f4f4f2 0%,#d9dad7 40%,rgba(255,255,255,0) 72%)"></div>
    <div class="abs band-dark" style="left:0;bottom:0;width:220px;height:62px"></div>
    <svg class="abs" style="left:0;bottom:0" width="220" height="30" viewBox="0 0 220 30"><path d="M0 30 L14 0 H220 V30 Z" fill="var(--slate)"/></svg>
    <div class="abs" style="left:8px;bottom:36px;width:206px;display:flex;justify-content:space-between">
      <span class="badge"><svg width="12" height="10" viewBox="0 0 12 10"><rect x="1" y="1" width="10" height="6" fill="none" stroke="#fff"/><path d="M4 9h4" stroke="#fff"/></svg>SCIENCE<br>DRIVEN</span>
      <span class="badge"><svg width="10" height="10" viewBox="0 0 10 10"><ellipse cx="5" cy="2" rx="4" ry="1.5" fill="none" stroke="#fff"/><path d="M1 2v6c0 1 8 1 8 0V2" fill="none" stroke="#fff"/></svg>EVIDENCE<br>BASED</span>
      <span class="badge"><svg width="10" height="10" viewBox="0 0 10 10"><circle cx="5" cy="5" r="4" fill="none" stroke="#fff"/><circle cx="5" cy="5" r="1.5" fill="#fff"/></svg>PATIENT<br>FOCUSED</span>
    </div>
    <div class="abs" style="left:20px;bottom:9px;width:194px;display:flex;justify-content:space-between;font-size:6.4px;font-weight:500;color:#fff">
      <span>(555) 014-2278</span><span>elenamarshdental.com</span>
    </div>
  </article>
</section>

</body>
</html>
```